Bold Creative Business Card for Digital Marketing Company (Contest)

NOTICE TO DESIGNERS: We understand this is how you make your living. Our commitment to you is to give you awesome and rapid feedback. If we don't think you are on the right track or have a chance of winning we will let you know right away so you don't have to focus your time with us and can continue to get work.

We respect the crowdsource community greatly. We have launched hundreds of crowdsource projects and will make this a great experience for you if you choose to participate (we hope you will!)

--------------
Brief
-------------

We are a cutting edge digital marketing company and we need a new, bold and creative business card designed to reflect who we are and what we do. We want our brand to stand out and be noticed.

The name of our company is: Tanglewood Web Marketing

Definition of Tanglewood:

a. a person pursuing rebellious, even potentially disruptive, policies or ideas:

b. a lone dissenter, as an intellectual, an artist, or a politician, who takes an independent stand apart from his or her associates

c. unorthodox, unconventional, nonconformist

Our businesses is helping small to medium size businesses with their online marketing using bold and creative outside the box strategies that get results.

We are an industry leader and need our business cards to stand out when we hand them out to people, and to be amazing so we stand out and "lead the pack"!

Our current website: http://www.tanglewoodwebmarketing.example

We are rebranding our site to reflect the new logo we just got but you will at least have an idea of who we are and what we do.

Colors We Want: We would like to see burnt Orange, Dark Blue, Gray and/or Black.

We need a front and back designed!

Be creative! Even to the point of creative-shaped business cards. Think outside the box. Let nothing stop your imagination! At the very least, we know that we want business cards that are not the US Standard 2"x3.5"... but rather the wider 3.35"x2.17" (European Standard) with rounded corners if you want to stick with a rectangular shape.

On the front we need:

Our Logo
Place for a name ie Paul Dravecki
Place for our phone number (612) 555 - 8806
Place for email name@tanglewoodwebmarketing.example
Place for our website www.TanglewoodWebMarketing.example

Optional... Place for a headshot photo of the person who the business card will be used for

On the back we need:

The wording... FREE VIDEO SERIES! "12 Smart Ideas To Improve Your Business Today!" www.TanglewoodWebMarketing.example/SmartIdeas

We are excited to see what you come up with.

Thank you for your interests and for participating in this contest!
Updates

Hi everyone! Thanks for all your submissions. However, we feel that most of you are "missing" what we're looking for. Almost all of the designs that have come in are what we would call "standard", "generic", or "typical". We are looking for something creative, different, attention-getting, a business card that would stand out amongst a stack of other business cards. I've shot this video: http://clipviewer.example/t/qWpZtRbHmsd Please take the time to review it. Let us know if you have questions. Thanks!

Target Market(s)

Our target market is small to medium sized business owners who need help with their online marketing.

Industry/Entity Type

Marketing

Font styles to use
Sans Serif

Colors
0355a3
85acd3
f78f20
f37022
faa54b
f68d4d

Requirements
Must have
• On the front we need:

Our Logo

Be CREATIVE! INTERESTING!

On the back we need:

Use the colors from our logo!
Nice to have
• Optional... Place for a headshot photo of the person who the business card will be used for.
Should not have
• Boring, "traditional" look and feel. We want and need to stand out!

```html
<!DOCTYPE html>
<html lang="en">
<head>
<meta charset="utf-8">
<title>Tanglewood Web Marketing – Business Card</title>
<link href="https://fonts.googleapis.com/css2?family=Lato:ital,wght@0,300;0,400;0,700;0,900;1,900&display=swap" rel="stylesheet">
<style>
  :root{
    --page:#e9e6e1;
    --card-black:#0b0b0c;
    --card-black-hi:#26272a;
    --card-blue:#1f5ea6;
    --card-blue-hi:#3a7cc4;
    --orange:#f37022;
    --orange-soft:#f68d4d;
    --sky:#85acd3;
    --white:#ffffff;
    --grey:#c9ccd1;
    --photo-a:#7f9bb8;
    --photo-b:#c8a58e;
  }
  *{box-sizing:border-box;margin:0;padding:0}
  html,body{width:1200px;height:1023px;overflow:hidden}
  body{background:var(--page);font-family:'Lato',sans-serif;position:relative}

  .card{
    position:absolute;left:320px;width:560px;height:363px;border-radius:26px;
    box-shadow:0 10px 24px rgba(0,0,0,.25);overflow:hidden;
  }
  .card--front{top:90px;background:linear-gradient(150deg,var(--card-black-hi) 0%,var(--card-black) 55%)}
  .card--back{top:560px;background:linear-gradient(150deg,var(--card-blue-hi) 0%,var(--card-blue) 60%)}

  .brand{position:absolute;display:flex;align-items:center;gap:14px}
  .brand__square{width:26px;height:26px;background:var(--orange);flex:none}
  .brand__name{color:var(--white);font-weight:700;line-height:1.05;letter-spacing:.5px}

  .card--front .brand{left:40px;top:128px}
  .card--front .brand__name{font-size:28px}

  .person{position:absolute;left:80px;top:210px}
  .person__name{color:var(--sky);font-weight:700;font-size:22px}
  .person__role{color:var(--grey);font-size:15px;margin-top:2px}

  .photo{
    position:absolute;right:36px;top:30px;width:118px;height:96px;border-radius:6px;
    border:4px solid #d9dadc;background:linear-gradient(135deg,var(--photo-a),var(--photo-b));
  }

  .contacts{position:absolute;left:250px;top:262px;list-style:none}
  .contacts li{display:flex;align-items:center;gap:10px;color:var(--white);font-size:15px;line-height:24px}
  .contacts svg{width:14px;height:14px;flex:none}

  .card--back .brand{left:50%;top:110px;transform:translateX(-50%)}
  .card--back .brand__name{font-size:40px}
  .tagline{
    position:absolute;left:0;right:0;bottom:36px;text-align:center;
    color:var(--orange);font-weight:900;font-style:italic;font-size:20px;
  }
</style>
</head>
<body>

<section class="card card--front" aria-label="Business card front">
  <div class="brand">
    <span class="brand__square"></span>
    <span class="brand__name">Tanglewood<br>Web Marketing</span>
  </div>

  <div class="person">
    <p class="person__name">Paul Dravecki</p>
    <p class="person__role">Director</p>
  </div>

  <div class="photo" role="img" aria-label="Headshot photo of the card holder"></div>

  <ul class="contacts">
    <li>
      <svg viewBox="0 0 14 14"><path d="M3 1h3l1 3-2 1.5a8 8 0 0 0 3.5 3.5L10 7l3 1v3a2 2 0 0 1-2 2A10 10 0 0 1 1 3a2 2 0 0 1 2-2z" fill="var(--grey)"/></svg>
      (612) 555 - 8806
    </li>
    <li>
      <svg viewBox="0 0 14 14"><rect x="1" y="1" width="12" height="12" fill="var(--sky)"/><path d="M3 7l3 3 5-6" stroke="var(--card-black)" stroke-width="1.6" fill="none"/></svg>
      name@tanglewoodwebmarketing.example
    </li>
    <li>
      <svg viewBox="0 0 14 14"><rect x="1.5" y="1.5" width="11" height="11" fill="none" stroke="var(--grey)" stroke-width="1.4"/></svg>
      www.TanglewoodWebMarketing.example
    </li>
  </ul>
</section>

<section class="card card--back" aria-label="Business card back">
  <div class="brand">
    <span class="brand__square"></span>
    <span class="brand__name">Tanglewood Web Marketing</span>
  </div>
  <p class="tagline">"12 Smart Ideas To Improve Your Business Today!"</p>
</section>

</body>
</html>
```